Looking for Landingpage / Website Designer

We are looking for a Web Designer / Developer for our upcoming Start Up Websites. The first project will be a simple responsive business website with a CTA- Button and an optional Newsletter Opt-In. We do aim for a modern online business approach, since we are a young company.

It is necessary to understand, that we need a conversion orientated design, not a wordpress blog with widgets and galleries.

We are currently discussing how it is going to happen and what preferences we need to focus on.

What we know is, that it should be more of a landing page with an option of adding 2 or 3 Navigation points.

We even thought about using services like pagemarlo.com or formvista.com to have an easier approach for future customizations and A/B testing.

We'd love to see how you fit the design/colors to the upcoming logo
(which is not the final version yet )

hope you can do something about that.

For the Structure.

1. Bracket

Slogan plus a preview text of what we are offering. On the right side a video placeholder plus CTA button.

2. Bracket

Illustrating 3 Benefits. On the right side - Opt in for Contact/Newsletter and CTA Button

3. Bracket

Picture with text just like you have it with the testimonial

You can orientate yourself towards to that landing page example as well:

http://cdn2.quentarix.net/hub/53/file-581676469-png/Blog-Related_Images/pagemarlo_landing_page.png?t=1416543075530

If our collaboration is going well, we would like to stay in touch for further projects.

Reason: There are 3 Design we do really like but, don't fit exactly our needs. 5 Days max.

Reason: For final adjustments.

I just uploaded the final logo :) Thank you for your commitment so far!

Target Market(s)

Our targeted audience could be almost everybody, who looks for an average paid side job (students, unemployed, house wives and whatever you can imagine). Maybe this is enough information for you to get a mere perception of what this is all about.

Industry/Entity Type

Business

Coding

Coded - Design and coding required

Font styles to use
Serif
Sans Serif

Colors
acd037
5c5c5c
33a6d7

Requirements
Must have
• Registration Opt-In
Responsive on any Device
Customizable
A benefits navigation just like in that example I've uploaded.
Nice to have
• As fast as possible ;D

```html
<!DOCTYPE html>
<html lang="en">
<head>
<meta charset="utf-8">
<title>Workvana.de – Job Search Services</title>
<link rel="stylesheet" href="https://fonts.googleapis.com/css2?family=Roboto:wght@400;500&family=Open+Sans:ital,wght@0,400;0,600;0,700;1,400&family=Oswald:wght@500&display=swap">
<style>
:root{
  --green:#8cab2f;
  --green-logo:#6db33f;
  --grey:#5c5c5c;
  --dark:#4a4a4a;
  --blue:#33a6d7;
  --blue-dark:#2b93c2;
  --orange:#ea5a0c;
  --orange-light:#f46d1c;
  --page:#efefef;
  --form-bg:#e2f1f8;
  --tint:#e6ebd3;
  --ink:#2f2f2f;
  --muted:#8a8a8a;
}
*{box-sizing:border-box;margin:0;padding:0}
html,body{width:986px;height:1200px;overflow:hidden}
body{position:relative;background:var(--page);font-family:"Open Sans",sans-serif;color:var(--ink)}
.abs{position:absolute}

.site-header{left:0;top:0;width:986px;height:87px;background:#fff}
.brand{left:169px;top:22px;display:flex;align-items:center;gap:8px;font-family:"Roboto",sans-serif;font-weight:500;font-size:34px;color:var(--green-logo);letter-spacing:-.5px;white-space:nowrap}
.brand-dot{width:42px;height:42px;border-radius:50%;background:var(--green-logo)}
.tagline{left:510px;top:36px;font-family:"Roboto",sans-serif;font-size:13.5px;color:var(--blue);white-space:nowrap}

.hero{left:0;top:87px;width:986px;height:370px;background:linear-gradient(100deg,#d9d2cb 0%,#a88d78 22%,#b7b06a 40%,#9aa07a 52%,#5b5b5e 62%,#c7c3bd 78%,#c89a66 100%)}
.hero-name{left:169px;top:146px;width:185px;height:40px;background:rgba(70,70,70,.85);color:#fff;font-family:"Roboto",sans-serif;font-size:29px;line-height:40px;padding-left:5px;letter-spacing:-.8px;white-space:nowrap;overflow:hidden}
.hero-title{left:169px;top:193px;width:319px;height:40px;background:var(--blue);color:#fff;font-family:"Roboto",sans-serif;font-weight:500;font-size:28px;line-height:40px;padding-left:6px;letter-spacing:-1px;white-space:nowrap;overflow:hidden}
.hero-copy{left:169px;top:245px;width:305px;color:#fff;font-size:11.3px;font-weight:600;line-height:17.5px}
.hero-copy p+p{margin-top:17px}
.btn{display:flex;align-items:center;justify-content:center;color:#fff;background:linear-gradient(var(--orange-light),var(--orange));border-radius:3px;box-shadow:0 2px 0 #b8440a;white-space:nowrap}
.btn-start{left:169px;top:375px;width:156px;height:33px;font-weight:700;font-size:13.5px}
.call{left:339px;top:380px;font-family:"Oswald",sans-serif;font-size:17px;color:#fff;letter-spacing:-.3px;white-space:nowrap}
.call span{color:var(--grey);margin-left:6px;font-weight:500}

.advice-band{left:0;top:457px;width:986px;height:88px;background:repeating-linear-gradient(135deg,#4d4d4d 0 3px,#474747 3px 6px)}
.advice{left:172px;top:480px;color:#fff;font-family:"Roboto",sans-serif;font-size:16.5px;line-height:20px;white-space:nowrap}

.signup{left:548px;top:113px;width:267px;height:508px;background:#f7f7f7;padding:8px}
.signup-inner{background:var(--form-bg);height:100%}
.signup-head{background:var(--green);color:#fff;font-family:"Roboto",sans-serif;font-weight:400;font-size:22px;line-height:26px;padding:7px 12px;height:70px}
.signup-lead{padding:7px 12px 0;font-family:"Roboto",sans-serif;font-size:13px;line-height:18px;color:var(--grey)}
.signup-sub{padding:4px 12px 0;font-size:9.6px;line-height:16px;color:var(--muted)}
.field{left:566px;width:230px;height:42px;border:1px solid #9ea4a8;background:#f2f9fc;font-size:11.5px;color:var(--grey);padding-left:8px;line-height:40px}
.btn-submit{left:566px;top:532px;width:225px;height:44px;font-size:18px;font-weight:700;border-radius:4px}
.privacy{left:548px;top:585px;width:260px;text-align:center;font-size:10.5px;color:var(--ink)}

.benefits{left:164px;top:564px;width:292px;list-style:none}
.benefit{position:relative;height:80px;padding:10px 0 0 50px}
.benefit.tinted{background:var(--tint);height:76px}
.benefit:nth-child(2){margin-top:4px}
.benefit:nth-child(3){margin-top:1px}
.benefit:nth-child(4){margin-top:6px}
.hex{position:absolute;left:6px;top:7px;width:33px;height:36px}
.hex span{position:absolute;inset:0;display:flex;align-items:center;justify-content:center;color:#fff;font-size:12px}
.benefit h3{font-family:"Roboto",sans-serif;font-weight:400;font-size:17px;color:var(--ink);margin-bottom:4px;white-space:nowrap}
.benefit p{font-size:10.3px;line-height:17.5px;color:var(--muted)}

.video{left:548px;top:642px;width:267px;height:220px;background:linear-gradient(120deg,#d8dde2,#5f6f80 45%,#2f3a48 70%,#a9b1ba)}
.play{left:655px;top:725px}

.testimonials{left:0;top:906px;width:986px;height:243px;background:var(--blue)}
.testimonials h2{position:absolute;left:169px;top:14px;font-family:"Roboto",sans-serif;font-weight:400;font-size:20.5px;color:#fff;white-space:nowrap}
.quote{top:957px;width:306px;height:116px;background:#fafafa;border:1px solid #d9e6ec;padding:10px 11px}
.quote h4{font-size:10px;font-weight:600;color:var(--grey);margin-bottom:8px}
.quote p{font-size:9.6px;line-height:16px;font-style:italic;color:var(--grey)}
.quote::after{content:"";position:absolute;left:30px;bottom:-9px;border-left:9px solid #fafafa;border-bottom:9px solid transparent}
.avatar{top:1090px;width:41px;height:41px}
.who{top:1099px;font-size:9.4px;line-height:15.5px;color:#fff;font-weight:600;white-space:nowrap}
.who b{color:#1d1d1d;font-weight:600;display:block}

.site-footer{left:0;top:1149px;width:986px;height:51px;background:repeating-linear-gradient(135deg,#2f98c6 0 2px,#2c91bd 2px 4px)}
.copy{left:184px;top:1167px;font-size:9.3px;color:#fff;white-space:nowrap}
.social{left:664px;top:1168px;display:flex;gap:15px}
.social span{width:13px;height:13px;border-radius:50%;background:#fff}
</style>
</head>
<body>

<header class="abs site-header">
  <div class="abs brand"><span class="brand-dot"></span>Workvana.de</div>
  <div class="abs tagline">Lorem ipsum dolor sit amet, consectetuer adipiscing</div>
</header>

<section class="abs hero" role="img" aria-label="Photo of a young woman working on a laptop at home"></section>
<div class="abs hero-name">Workvana.de</div>
<h1 class="abs hero-title">#1 Job Search Services</h1>
<svg class="abs" style="left:378px;top:146px" width="108" height="25" viewBox="0 0 108 25" aria-hidden="true">
  <path d="M2 8 C30 -2 70 0 100 14" fill="none" stroke="#fff" stroke-width="1.6" stroke-dasharray="2 3"/>
  <path d="M97 8 L104 18 L93 17 Z" fill="#fff"/>
</svg>
<div class="abs hero-copy">
  <p>Lorem ipsum dolor sit amet, consectetuer adipiscing elit, sed diam nonummy nibh euismod tincidunt ut ero eros et accumsan et iusto odio.Duis autem vel eum iriure dolor in hendrerit in</p>
  <p>vulputate velit esse molestie consequat, vel illum dolore eu feugiat nulla facilisis at</p>
</div>
<a class="abs btn btn-start">Get Started</a>
<div class="abs call">Call Us<span>0800 555 0199</span></div>

<section class="abs advice-band"></section>
<p class="abs advice">Free Advice By Workvana.de your<br>free career advicer</p>
<svg class="abs" style="left:408px;top:505px" width="132" height="62" viewBox="0 0 132 62" aria-hidden="true">
  <path d="M2 2 C30 40 70 54 122 55" fill="none" stroke="#9a9a9a" stroke-width="1.6" stroke-dasharray="2 3"/>
  <path d="M122 50 L130 55 L122 61 Z" fill="#9a9a9a"/>
</svg>

<aside class="abs signup">
  <div class="signup-inner">
    <h2 class="signup-head">Workvana 30 Days To Higher Marketing</h2>
    <p class="signup-lead">Duis autem vel eum iriure dolor in hendrerit in vulputate velit esse molestie consequat</p>
    <p class="signup-sub">Lorem ipsum dolor sit amet, consectetuer adipiscing elit  molestie consequat,</p>
  </div>
</aside>
<div class="abs field" style="top:299px">First Name</div>
<div class="abs field" style="top:357px">Email</div>
<div class="abs field" style="top:414px">Company Name</div>
<div class="abs field" style="top:473px">Phone Number</div>
<a class="abs btn btn-submit">Submit Now</a>
<p class="abs privacy">100% Privacy Guaranteed</p>

<ol class="abs benefits">
  <li class="benefit tinted">
    <svg class="hex" viewBox="0 0 33 36"><path d="M16.5 0 L33 9 V27 L16.5 36 L0 27 V9 Z" fill="#33a6d7"/></svg><span class="hex"><span>1</span></span>
    <h3>Lorem Ipsum dolor sitamet</h3>
    <p>Lorem ipsum dolor sit amet, consectetuer adipis cing elit, sed diam nonummy</p>
  </li>
  <li class="benefit">
    <svg class="hex" viewBox="0 0 33 36"><path d="M16.5 0 L33 9 V27 L16.5 36 L0 27 V9 Z" fill="#33a6d7"/></svg><span class="hex"><span>2</span></span>
    <h3>Duis autem vel eum redolor</h3>
    <p>Lorem ipsum dolor sit amet, consectetuer adipis cing elit, sed diam nonummy</p>
  </li>
  <li class="benefit tinted">
    <svg class="hex" viewBox="0 0 33 36"><path d="M16.5 0 L33 9 V27 L16.5 36 L0 27 V9 Z" fill="#33a6d7"/></svg><span class="hex"><span>3</span></span>
    <h3>Claritas est etiam processus</h3>
    <p>Lorem ipsum dolor sit amet, consectetuer adipis cing elit, sed diam nonummy</p>
  </li>
  <li class="benefit">
    <svg class="hex" viewBox="0 0 33 36"><path d="M16.5 0 L33 9 V27 L16.5 36 L0 27 V9 Z" fill="#33a6d7"/></svg><span class="hex"><span>4</span></span>
    <h3>Vulputate velit esse molestie con</h3>
    <p>Lorem ipsum dolor sit amet, consectetuer adipis cing elit, sed diam nonummy</p>
  </li>
</ol>

<div class="abs video" role="img" aria-label="Video still of two businessmen reviewing documents"></div>
<svg class="abs play" width="50" height="50" viewBox="0 0 50 50" aria-hidden="true">
  <circle cx="25" cy="25" r="21" fill="none" stroke="#fff" stroke-width="4"/>
  <path d="M20 14 L35 25 L20 36 Z" fill="#fff"/>
</svg>

<section class="abs testimonials"><h2>What Our Customers Have to Say</h2></section>
<blockquote class="abs quote" style="left:169px">
  <h4>LOREM IPSUM DOLOR</h4>
  <p>Lorem ipsum dolor sit amet, consectetuer adipiscing elit, sed diam nonummy nibh euismod tincidunt ut laoreet dolore magna aliquam erat volutpat. Ut wisi enim ad minim veniam,</p>
</blockquote>
<blockquote class="abs quote" style="left:513px">
  <h4>LOREM IPSUM DOLOR</h4>
  <p>Lorem ipsum dolor sit amet, consectetuer adipiscing elit, sed diam nonummy nibh euismod tincidunt ut laoreet dolore magna aliquam erat volutpat. Ut wisi enim ad minim veniam,</p>
</blockquote>
<div class="abs avatar" style="left:181px;background:linear-gradient(#6b5a4c,#c09a7c)" role="img" aria-label="Customer portrait photo"></div>
<div class="abs who" style="left:230px"><b>Jan Doell</b>05 October 2013</div>
<div class="abs avatar" style="left:523px;background:linear-gradient(#8a7560,#e0c2a4)" role="img" aria-label="Customer portrait photo"></div>
<div class="abs who" style="left:572px"><b>Jan Doell</b>05 October 2013</div>

<footer class="abs site-footer"></footer>
<p class="abs copy">Copyright © 2014 Tidy Nook All rights reserved.</p>
<div class="abs social" aria-label="Social links"><span></span><span></span><span></span><span></span><span></span><span></span></div>

</body>
</html>
```